Makeupbyfernandflick banner

Hi I am a makeup artist looking at getting my banner created, I will be sending a picture below as a example of what I want, it's what an other makeup artist has done on her banner and I love it !
I will be also sending the pictures that you will need to put it together and will also attach a picture of what I would want written in the middle, please try and match the writing showen in the example.
Please feel free to ask any questions
Thank you
Marlene Tobrecht

```html
<!DOCTYPE html>
<html lang="en">
<head>
<meta charset="utf-8">
<title>Makeupbyfernandflick banner</title>
<link rel="stylesheet" href="https://fonts.googleapis.com/css2?family=Questrial&family=Poppins:wght@500;600&display=swap">
<style>
  :root {
    --ink: #111111;
    --accent: #e8333a;
    --accent-soft: #f06a6a;
    --lip-deep: #d8232b;
    --lip-light: #f7b9b9;
    --paper: #ffffff;
    --powder: #8d8d8d;
    --powder-light: #e4e4e4;
    --muted: #555555;
  }
  html, body {
    margin: 0;
    padding: 0;
    width: 1200px;
    height: 2742px;
    overflow: hidden;
    background: var(--paper);
  }
  .banner {
    position: relative;
    width: 1200px;
    height: 2742px;
    background: var(--paper);
    font-family: "Questrial", "Century Gothic", sans-serif;
    color: var(--ink);
    overflow: hidden;
  }
  .lips-artwork {
    position: absolute;
    left: 88px;
    top: 38px;
    width: 1037px;
    height: 687px;
    border-radius: 50%;
    background: radial-gradient(ellipse at center, var(--lip-deep) 0%, var(--accent-soft) 45%, var(--lip-light) 68%, rgba(255,255,255,0) 72%);
  }
  .brand-name {
    position: absolute;
    left: 0;
    width: 1200px;
    top: 340px;
    text-align: center;
    font-size: 76px;
    line-height: 1;
    color: var(--ink);
  }
  .artist-name {
    position: absolute;
    top: 845px;
    width: 100%;
    margin: 0;
    font-weight: 400;
    text-align: center;
    font-size: 116px;
    line-height: 1;
    letter-spacing: -2px;
  }
  .artist-role {
    position: absolute;
    top: 982px;
    width: 100%;
    text-align: center;
    font-size: 88px;
    line-height: 1;
    letter-spacing: -1px;
  }
  .highlight { color: var(--accent); }
  .tagline {
    position: absolute;
    top: 1138px;
    width: 100%;
    margin: 0;
    text-align: center;
    font-family: "Poppins", "Century Gothic", sans-serif;
    font-weight: 600;
    font-size: 60px;
    line-height: 1;
  }
  .tagline .highlight { color: var(--accent-soft); }
  .bio {
    position: absolute;
    top: 1278px;
    left: 40px;
    width: 1120px;
    margin: 0;
    text-align: center;
    white-space: nowrap;
    font-size: 35px;
    line-height: 57.5px;
    color: var(--ink);
  }
  .phone {
    position: absolute;
    top: 1700px;
    width: 100%;
    text-align: center;
    font-family: "Poppins", "Century Gothic", sans-serif;
    font-weight: 500;
    font-size: 66px;
    line-height: 1;
  }
  .email {
    position: absolute;
    top: 1792px;
    width: 100%;
    text-align: center;
    font-size: 54px;
    line-height: 1;
  }
  .social {
    position: absolute;
    top: 1918px;
    left: 0;
    width: 100%;
    display: flex;
    justify-content: center;
    gap: 60px;
    align-items: center;
  }
  .social-item {
    display: flex;
    align-items: center;
    gap: 16px;
    font-size: 48px;
    color: var(--muted);
  }
  .social-mark {
    width: 62px;
    height: 62px;
    background: var(--muted);
  }
  .brush-photo {
    position: absolute;
    left: 325px;
    top: 2050px;
    width: 875px;
    height: 692px;
    background: radial-gradient(ellipse at 45% 55%, var(--powder) 0%, var(--powder-light) 55%, rgba(255,255,255,0) 80%);
  }
</style>
</head>
<body>
  <main class="banner">
    <div class="lips-artwork" role="img" aria-label="Red lipstick kiss print illustration"></div>
    <div class="brand-name">Makeupbyfernandflick</div>

    <h1 class="artist-name">Marlene <span class="highlight">Tobrecht</span></h1>
    <div class="artist-role">Make-up <span class="highlight">Artist</span></div>

    <h2 class="tagline">Specialising in all <span class="highlight">things makeup</span></h2>

    <p class="bio">Marlene is a qualified makeup artist based in Sydney, her<br>experience within the makeup industry of over 5 years.<br>Marlene’s impeccable makeup shows through her work and<br>her clientele old and new becoming not just clients but<br>friends her personality is not only bubbly and friendly but also<br>warm and very caring she pays a lot of her attention to<br>detail and will perfect each looks as the client requests.</p>

    <div class="phone">0412555018</div>
    <div class="email">makeupbyfernandflick@mailpost.com</div>

    <div class="social">
      <div class="social-item"><span class="social-mark"></span>Chatterbox</div>
      <div class="social-item"><span class="social-mark"></span>Lenslog</div>
    </div>

    <div class="brush-photo" role="img" aria-label="Photograph of a makeup brush with scattered loose powder"></div>
  </main>
</body>
</html>
```